THE TALL COPPER ATLAS OF PORTS

subtitle: AN INTRO TO SEARCH ENGINE OPTIMIZATION
background: white
dimensions: 1562x2500

Target Market(s)

Marketing professionals

Industry/Entity Type

Digital Marketing

Font styles to use
Sans Serif

Colors
ffffff
1b1b1b
3176b5

Requirements
Should not have
• Images or graphics

```html
<!DOCTYPE html>
<html lang="en">
<head>
<meta charset="utf-8">
<title>The Tall Copper Atlas of Ports</title>
<link rel="stylesheet" href="https://fonts.googleapis.com/css2?family=Antonio:wght@500;600;700&family=Open+Sans:wght@400&display=swap">
<style>
  :root {
    --paper: #ffffff;
    --ink: #1b1b1b;
    --brand-blue: #3176b5;
    --muted: #6b6b6b;
    --field: #eceded;
    --field-border: #dcdedf;
    --button: #b3cde6;
    --icon: #9a9a9a;
  }
  * { margin: 0; padding: 0; box-sizing: border-box; }
  html, body {
    width: 750px;
    height: 1200px;
    overflow: hidden;
    background: var(--paper);
  }
  .cover {
    position: relative;
    width: 750px;
    height: 1200px;
    background: var(--paper);
    font-family: "Antonio", "Arial Narrow", sans-serif;
  }
  .search-bar {
    position: absolute;
    left: 122px;
    top: 128px;
    width: 506px;
    height: 52px;
    border: 2px solid var(--field-border);
    border-radius: 4px;
    background: var(--paper);
    padding: 3px;
    display: flex;
  }
  .search-field {
    flex: 1;
    background: var(--field);
    display: flex;
    align-items: center;
    padding-left: 16px;
    font-family: "Open Sans", Arial, sans-serif;
    font-size: 22px;
    color: #666;
  }
  .search-field svg { margin-right: 12px; }
  .search-button {
    width: 100px;
    background: var(--button);
    border-radius: 3px;
    display: flex;
    align-items: center;
    justify-content: center;
    font-family: "Open Sans", Arial, sans-serif;
    font-size: 22px;
    color: #555;
  }
  .title {
    position: absolute;
    left: 64px;
    top: 306px;
    color: var(--brand-blue);
    font-weight: 700;
    font-size: 82px;
    line-height: 100px;
    letter-spacing: -3px;
  }
  .title-line { display: block; white-space: nowrap; }
  .title-keyword {
    position: absolute;
    left: 64px;
    top: 520px;
    width: 428px;
    height: 296px;
    overflow: visible;
  }
  .subtitle {
    position: absolute;
    left: 67px;
    top: 822px;
    font-size: 32px;
    line-height: 40px;
    font-weight: 600;
    color: var(--muted);
    letter-spacing: 0.4px;
    white-space: nowrap;
  }
  .rule {
    position: absolute;
    left: 0;
    top: 1093px;
    width: 487px;
    height: 6px;
    background: var(--brand-blue);
  }
  .author {
    position: absolute;
    right: 263px;
    top: 1106px;
    font-size: 36px;
    line-height: 44px;
    font-weight: 600;
    color: var(--ink);
    white-space: nowrap;
  }
</style>
</head>
<body>
  <main class="cover">
    <div class="search-bar">
      <div class="search-field">
        <svg width="32" height="32" viewBox="0 0 32 32" aria-hidden="true">
          <circle cx="13" cy="13" r="9" fill="none" stroke="var(--icon)" stroke-width="4"/>
          <line x1="20" y1="20" x2="29" y2="29" stroke="var(--icon)" stroke-width="5" stroke-linecap="round"/>
        </svg>
        www.
      </div>
      <div class="search-button">Search</div>
    </div>

    <h1 class="title">
      <span class="title-line">The Tall</span>
      <span class="title-line">Copper Atlas of</span>
    </h1>

    <svg class="title-keyword" viewBox="0 0 428 296" aria-label="Ports">
      <text x="3" y="290" textLength="422" lengthAdjust="spacingAndGlyphs"
            font-family="Antonio, 'Arial Narrow', sans-serif" font-weight="700"
            font-size="318" fill="var(--brand-blue)"
            stroke="var(--brand-blue)" stroke-width="5" stroke-linejoin="round">PORTS</text>
    </svg>

    <p class="subtitle">Logic between the search engine,<br>and the searcher...</p>

    <div class="rule"></div>
    <p class="author">Author Name</p>
  </main>
</body>
</html>
```